Innovative Nutritionist Needs a product name and label design

I need a label design for a new mineral product for elite racehorses. This is an innovative product that combines a bunch of important minerals for racehorses and vitally, delays or prevents fatigue. Racehorses are usually confined to stables and are fed grains and hay and miss out on the essential nutrients unequal offered by grass. My product provides those minerals usually obtained from grass. Packaging is an important consideration. The product will be in individual dose, foil sachets. Im not married to the power colours (gold, silver, black) necessarily, but the label must allow for adhesion to any of these colours. I want the label to ooze power, success, elite, winner!

Target Market(s)

racehorse trainers, veterinarians, owners

Industry/Entity Type

Nutritionist

Font styles to use
Other font styles liked:
• entirely flexible

Requirements
Must have
• Must have a strong presence. Must communicate an edge, vitality, health, power.
• The activity level of the minerals in the product is communicated in electrical units - milliequivalents/100g - so make of that what you can
Nice to have
• Not much to contribute here, but could contain a silhouette of a horse powering past the winning post.
• The activity level of the minerals in the product is communicated in electrical units - milliequivalents/100g -
Should not have
• anything passive, insipid, corny, cartoonish

```html
<!DOCTYPE html>
<html lang="en">
<head>
<meta charset="UTF-8">
<title>Surge – Racehorse Mineral Supplement Label</title>
<link rel="stylesheet" href="https://fonts.googleapis.com/css2?family=Big+Shoulders+Display:wght@400;900&family=Bebas+Neue&display=swap">
<style>
  :root {
    --navy-deep: #0b2f4d;
    --navy: #124468;
    --navy-glow: #1d6189;
    --frame-silver: #b9c0c7;
    --panel-top: #6e6e72;
    --panel-bottom: #ffffff;
    --horse-teal: rgba(28, 109, 143, 0.9);
    --horse-navy: rgba(14, 53, 86, 0.9);
    --wordmark: #0f3a5c;
    --units-text: #c9d0d7;
    --body-text: #eef1f3;
    --bar-light: #f4f5f6;
    --bar-mid: #9aa1a8;
  }
  * { margin: 0; padding: 0; box-sizing: border-box; }
  html, body {
    width: 1200px;
    height: 777px;
    overflow: hidden;
    background: var(--navy-deep);
  }
  .label {
    position: relative;
    width: 1200px;
    height: 777px;
    background: radial-gradient(ellipse at 55% 70%, var(--navy-glow) 0%, var(--navy) 45%, var(--navy-deep) 100%);
    overflow: hidden;
  }
  .label__frame {
    position: absolute;
    left: 17px; top: 17px;
    width: 1166px; height: 743px;
    border: 4px solid var(--frame-silver);
  }
  .label__panel {
    position: absolute;
    left: 40px; top: 42px;
    width: 1122px; height: 492px;
    background: linear-gradient(to bottom, var(--panel-top) 0%, #bdbdc0 45%, var(--panel-bottom) 100%);
    overflow: hidden;
  }
  .label__horse {
    position: absolute;
    left: 350px; top: 60px;
    width: 760px; height: 432px;
    background:
      radial-gradient(ellipse 60% 70% at 60% 60%, var(--horse-navy) 0%, var(--horse-teal) 45%, rgba(28, 109, 143, 0) 75%);
  }
  .label__name {
    position: absolute;
    left: 54px; top: 368px;
    font-family: "Big Shoulders Display", sans-serif;
    font-weight: 900;
    font-size: 196px;
    line-height: 1;
    letter-spacing: 4px;
    color: var(--wordmark);
    text-shadow: 5px 3px 0 #ffffff, 8px 5px 0 var(--wordmark);
  }
  .label__bar {
    position: absolute;
    left: 55px; top: 552px;
    width: 502px; height: 13px;
    background: linear-gradient(to bottom, var(--bar-light) 0%, var(--bar-mid) 55%, var(--bar-light) 100%);
  }
  .label__units {
    position: absolute;
    left: 55px; top: 577px;
    font-family: "Big Shoulders Display", sans-serif;
    font-weight: 400;
    font-size: 38px;
    line-height: 1;
    letter-spacing: 1.5px;
    color: var(--units-text);
  }
  .label__ingredients {
    position: absolute;
    left: 55px; top: 620px;
    width: 1110px;
    font-family: "Bebas Neue", sans-serif;
    font-size: 21px;
    line-height: 37px;
    letter-spacing: 0.5px;
    color: var(--body-text);
    white-space: nowrap;
  }
</style>
</head>
<body>
  <main class="label">
    <div class="label__frame"></div>
    <section class="label__panel">
      <div class="label__horse" role="img" aria-label="Silhouette of a galloping racehorse with flowing mane and tail"></div>
    </section>
    <h1 class="label__name">SURGE</h1>
    <div class="label__bar"></div>
    <h2 class="label__units">UNITS - MILLIEQUIVALENTS/100G</h2>
    <p class="label__ingredients">MINERALS AND AMINO ACIDS WITH 7.5 MG OF BIOTIN, 1,250 MG GLUCOSAMINE, 25 MG HYALURONIC ACID, 5,000 MG OF MSM,<br>1,000 MG DEVIL'S CLAW, 250 MG BOSWELLIA, 25 MG GRAPE SEED EXTRACT, 125 MG VITAMIN C AND 1,750 IU OF VITAMIN E,<br>1.5 MG OF CHROMIUM AND 3,105 MG OF MAGNESIUM PER 2.5 OUNCES AND COMES IN A TASTY PELLET FORM</p>
  </main>
</body>
</html>
```